Fatigued and Overloaded by COVID Messages? We need original illustrations to show that.

Everywhere you look there are messages about COVID. That is leading many people to feel fatigued and overloaded by the messages.

We surveyed U.S. adults March 20th - 24th, 2020 and measured message fatigue, information overload, perceived repetition, and perceived exaggeration. Here is how participants responded:

When it comes to coronavirus . . .
55% feel exhausted by all the messages.
54% feel overloaded by the amount of information.
51% feel that the messages are repetitive.
47% feel like messages exaggerate how bad it is.

In other words, almost half of U.S. adults show signs of message fatigue, information overload, perceived message repetition, and perceived message exaggeration.

We will continue to survey 400 adults every week for the next 16 weeks. Each time we will measure message fatigue, information overload, perceived repetition, and perceived exaggeration. We expect that it will increase over time.

What are we looking for? We need innovative and original illustrations that attempt to communicate these findings. The illustrations would visualize message fatigue, information overload, perceived message repetition, and perceived message exaggeration.

What sort of visual are we looking for? Our preference is for an original illustration (or set of illustrations). Our preference is for creative and powerful illustrations, but we are also open to the creative and well-executed infographics.

We need these images fast . We will award monetary prizes to the 3 best designs. If we like more than that, then we might purchase more (e.g., in past contests, we have purchased as many as 30 designs).

What we will need:
(1) The illustrations must be original and we will need the photoshop and/or illustrator files for all artwork. (By original, we mean that the illustrations are 100% created by you. Our organization requires that we utilize only original illustrated work. We have had issues with free imagery being pirated and reposted as free. We sidestep that issue by just having everything created.)

(2) The illustration should say, somewhere: "Based on a survey of 400 U.S. adults conducted March 20 - 24th, 2020."

(3) We will have almost 4 months worth of data by the time this is done. In other words, the illustrations might be able to help us present that weekly data.

(4) We have conducted other Artquarry projects. It might be helpful to examine designs we liked in the past. For example, here is another COVID project we just finished:

https://jobs.artquarry-example.com/job/5172846

Target Market(s)

U.S. adults

Requirements
Must have
• Original illustrations. Mobile friendly design. People will view this on their smartphones.
Nice to have
• A design that we can use to communicate the data across time.

```html
<!DOCTYPE html>
<html lang="en">
<head>
<meta charset="utf-8">
<title>Fatigued and Overloaded by COVID Messages?</title>
<link href="https://fonts.googleapis.com/css2?family=Montserrat:ital,wght@0,500;0,600;0,700;0,800;1,600&display=swap" rel="stylesheet">
<style>
  :root {
    --brand-blue: #0567ae;
    --pie-blue: #57a8cc;
    --alert-red: #e34a3f;
    --band-grey: #d1d2d4;
    --ink: #111111;
    --paper: #ffffff;
    --figure-fill: rgba(255, 255, 255, 0.55);
  }
  * { margin: 0; padding: 0; box-sizing: border-box; }
  html, body { width: 848px; height: 1200px; overflow: hidden; background: var(--paper); }
  body { font-family: "Montserrat", Arial, sans-serif; color: var(--ink); position: relative; }

  .masthead {
    position: absolute; left: 0; top: 0; width: 848px; height: 170px;
    background: var(--brand-blue); color: var(--paper); text-align: center;
  }
  .masthead__title {
    position: absolute; left: 0; right: 0; top: 36px;
    font-weight: 800; font-size: 31px; line-height: 34px; letter-spacing: 0.3px;
  }
  .masthead__intro {
    position: absolute; left: 0; right: 0; top: 114px;
    font-style: italic; font-weight: 600; font-size: 10.5px; line-height: 13px;
  }

  .lead {
    position: absolute; left: 0; right: 0; top: 184px; text-align: center;
    font-weight: 700; font-size: 23px;
  }

  .stat { position: absolute; width: 300px; text-align: center; }
  .stat__chart { display: block; margin: 0 auto; }
  .stat__value {
    font-weight: 800; font-size: 42px; line-height: 44px; color: var(--alert-red);
    margin-top: 6px;
  }
  .stat__label { font-weight: 500; font-size: 16.5px; line-height: 19.5px; margin-top: 16px; }

  .stat--exhausted { left: 112px; top: 233px; }
  .stat--overloaded { left: 465px; top: 233px; }
  .stat--repetitive { left: 112px; top: 631px; }
  .stat--exaggerated { left: 465px; top: 631px; }
  .stat--exhausted .stat__label { padding-left: 22px; }
  .stat--overloaded .stat__label { padding-left: 36px; }
  .stat--repetitive .stat__label { padding-left: 14px; }
  .stat--exaggerated .stat__label { padding-left: 26px; }

  .summary {
    position: absolute; left: 0; top: 1011px; width: 848px; height: 152px;
    background: var(--band-grey);
  }
  .summary__map {
    position: absolute; left: 130px; top: 42px; width: 142px; height: 78px;
    background: linear-gradient(90deg, var(--pie-blue) 0 50%, var(--alert-red) 50% 100%);
    border-radius: 10px 14px 22px 18px;
  }
  .summary__heading {
    position: absolute; left: 289px; top: 34px; font-weight: 700; font-size: 19px;
  }
  .summary__text {
    position: absolute; left: 287px; top: 59px; width: 470px; white-space: nowrap;
    font-weight: 500; font-size: 16.3px; line-height: 19.5px;
  }

  .source {
    position: absolute; left: 0; top: 1163px; width: 848px; height: 37px;
    background: var(--brand-blue); color: var(--paper); text-align: center;
    font-weight: 500; font-size: 13.5px; line-height: 37px;
  }
</style>
</head>
<body>
  <header class="masthead">
    <h1 class="masthead__title">FATIGUED AND OVERLOADED<br>BY COVID MESSAGES?</h1>
    <p class="masthead__intro">We surveyed U.S. adults March 20th - 24th, 2020 and<br>measured message fatigue, information overload,<br>perceived repetition, and perceived exaggeration.</p>
  </header>

  <h2 class="lead">When it comes to coronavirus . . .</h2>

  <section class="stat stat--exhausted">
    <svg class="stat__chart" width="236" height="236" viewBox="-118 -118 236 236">
      <circle r="114" fill="var(--pie-blue)"/>
      <path d="M0,0 L0,-114 A114,114 0 1 0 35.2,108.4 Z" fill="var(--alert-red)"/>
      <rect x="-44" y="-6" width="76" height="120" rx="10" fill="var(--figure-fill)" role="img" aria-label="Drawn figure looking wearily at a phone"/>
    </svg>
    <div class="stat__value">55%</div>
    <p class="stat__label">feel exhausted by<br>all the messages</p>
  </section>

  <section class="stat stat--overloaded">
    <svg class="stat__chart" width="236" height="236" viewBox="-118 -118 236 236">
      <circle r="114" fill="var(--pie-blue)"/>
      <path d="M0,0 L0,-114 A114,114 0 1 0 28.4,110.4 Z" fill="var(--alert-red)"/>
      <rect x="-80" y="6" width="146" height="106" rx="10" fill="var(--figure-fill)" role="img" aria-label="Drawn figure at a laptop surrounded by notification icons"/>
    </svg>
    <div class="stat__value">54%</div>
    <p class="stat__label">feel overloaded<br>by the amount<br>of information</p>
  </section>

  <section class="stat stat--repetitive">
    <svg class="stat__chart" width="236" height="236" viewBox="-118 -118 236 236">
      <circle r="114" fill="var(--pie-blue)"/>
      <path d="M0,0 L0,-114 A114,114 0 1 0 7.2,113.8 Z" fill="var(--alert-red)"/>
      <rect x="-14" y="2" width="80" height="112" rx="10" fill="var(--figure-fill)" role="img" aria-label="Drawn figure with a phone as repeated arrows fly past"/>
    </svg>
    <div class="stat__value">51%</div>
    <p class="stat__label">feel that the messages<br>are repetitive</p>
  </section>

  <section class="stat stat--exaggerated">
    <svg class="stat__chart" width="236" height="236" viewBox="-118 -118 236 236">
      <circle r="114" fill="var(--pie-blue)"/>
      <path d="M0,0 L0,-114 A114,114 0 0 0 -21.4,112 Z" fill="var(--alert-red)"/>
      <rect x="-14" y="12" width="70" height="102" rx="10" fill="var(--figure-fill)" role="img" aria-label="Drawn figure with a phone surrounded by alarming news symbols"/>
    </svg>
    <div class="stat__value">47%</div>
    <p class="stat__label">feel like messages<br>exaggerate how bad it is</p>
  </section>

  <section class="summary">
    <div class="summary__map" role="img" aria-label="Map of the United States, half blue and half red"></div>
    <h3 class="summary__heading">In other words</h3>
    <p class="summary__text">almost half of U.S. adults show signs of message<br>fatigue, information overload, perceived message<br>repetition, and perceived message exaggeration.</p>
  </section>

  <footer class="source">Based on a survey of 400 U.S. adults conducted March 20 - 24th, 2020</footer>
</body>
</html>
```